Tri-fold Brochure Design for Law Firm

I need a tri-fold brochure to give to prospective clients.
I have attached a Photoshop design file of a tri-fold brochure. The content (copy) is good, however, he brochure itself looks very amateurish.
I want a professional, sophisticated looking brochure.
The law firm specializes in commercial debt collection.
The law firm is located in New York City.
Our target market is business owners, doctors, lawyers, collection agencies and accountants.
Visit my website which is being designed at www.dorvenlaw.com. I like the font used for the name of my company and the rich blue color used.

Target Market(s)

Business Owners, Doctors, Law Firms and Accountants

Industry/Entity Type

Law Firm

Font styles to use
Serif

Requirements
Must have
• Professional quality graphic work. Attention to details.
• PHOTOGRAPHS ONLY, NO CLIP-ART.
• DARK COLORS - NAVY BLUE, HUNTER GREEN, BLACK, GRAY & WHITE
Nice to have
• I want it to look smart, modern and sophisticated.
• Visit my website which is being designed at www.dorvenlaw.com. I like the font used for the name of my company and the rich blue color used.
Should not have
• Bad artwork
• CLIP ART

```html
<!DOCTYPE html>
<html lang="en">
<head>
<meta charset="utf-8">
<title>Dorven &amp; Company PLLC – Tri-fold Brochure</title>
<link href="https://fonts.googleapis.com/css2?family=Libre+Baskerville:wght@700&family=Open+Sans:wght@400;600;700&display=swap" rel="stylesheet">
<style>
:root{
  --blue:#1f5aa8;
  --navy:#17376e;
  --ink:#222;
  --paper:#fff;
  --bg:#dcdcdc;
}
*{box-sizing:border-box;margin:0;padding:0}
html,body{width:1200px;height:960px;overflow:hidden}
body{background:var(--bg);font-family:"Open Sans",sans-serif;color:var(--ink);position:relative}
.sheet{position:absolute;top:255px;width:570px;height:450px;background:var(--paper);display:flex;box-shadow:0 6px 18px rgba(0,0,0,.25);overflow:hidden}
.sheet--outside{left:20px}
.sheet--inside{left:610px}
.panel{width:190px;height:100%;position:relative;padding:12px 11px;font-size:6px;line-height:1.32;overflow:hidden}
.panel p{margin-bottom:4px;text-align:justify}
.tab{display:inline-block;background:var(--blue);color:#fff;font-family:"Libre Baskerville",serif;font-weight:700;text-transform:uppercase;font-size:9px;padding:3px 8px;margin:4px 0 5px;border-radius:0 6px 0 6px;box-shadow:2px 2px 0 var(--navy)}
.tab--sm{font-size:6.6px}
.serve{list-style:none;margin:2px 0 4px 6px;font-weight:600;font-size:6.2px}
.serve li::before{content:"• "}
.fees{list-style:none;margin:2px 0 5px 6px}
.fees li::before{content:"• "}
.wave{position:absolute;left:0;bottom:0;width:190px;height:60px}
.photo{position:absolute}
.photo--city{inset:0;background:linear-gradient(180deg,#e9eaec 0%,#b9bcc2 45%,#d6d8dc 100%)}
.photo--library{left:0;right:0;top:190px;height:150px;background:linear-gradient(135deg,#0f2d5c,#3f78bf 55%,#0f2d5c)}
.photo--building{left:0;right:0;bottom:0;height:78px;background:linear-gradient(180deg,#7d8087,#e6e7e9 40%,#50545b)}
.photo--gavel{left:0;right:0;top:0;height:120px;background:linear-gradient(160deg,#2a1a10,#8a4e22 55%,#3b2415)}
.contact{position:relative;z-index:1;text-align:center;color:var(--navy);padding-top:30px}
.firm{font-family:"Open Sans",sans-serif;font-weight:700;color:var(--navy);line-height:1.15}
.contact .firm{font-size:15px}
.tag{font-size:5px;color:var(--blue);margin:3px 0 8px}
.who{font-weight:700;font-size:7px;margin-top:2px}
.contact .line{font-size:6.4px}
.office{font-weight:700;font-size:7.6px;margin:16px 0 3px;text-transform:uppercase}
.web{font-weight:700;letter-spacing:2px;font-size:7px;margin-top:18px}
.call{display:flex;align-items:center;gap:6px;background:var(--blue);color:#fff;border-radius:20px;margin:8px 6px 0;padding:5px 8px;text-align:left;font-weight:700;font-size:6.4px}
.call svg{flex:none}
.cover-head{text-align:center;padding-top:12px}
.cover-head .firm{font-size:11px}
.cover-head .sub{font-size:7px;color:var(--ink);margin-top:3px}
.cover-shape{position:absolute;left:0;top:70px;width:190px;height:320px}
.cover-phone{position:absolute;left:0;right:0;bottom:14px;display:flex;align-items:center;justify-content:center;gap:8px;color:var(--blue);font-weight:700;font-size:15px}
</style>
</head>
<body>

<section class="sheet sheet--outside">
  <div class="panel">
    <span class="tab">A Trusted Partner</span>
    <p>We under the business of debt collection. Our primary focus is to help our clients secure the payments they are owed. We work closely with both private clients and leading service professionals, such as attorneys and accountants, to provide added value to their clients through customized debt collection services.</p>
    <p>We value our relationships as trusted advisors.</p>
    <p><strong>We proudly serve:</strong></p>
    <ul class="serve">
      <li>Law firms</li><li>Accounting Firms</li><li>Manufacturers</li><li>Wholesalers and Distributors</li><li>Collection Agencies</li><li>Financial Service Companies</li><li>Factors</li><li>Doctors and Healthcare Professionals</li><li>Carting Companies</li><li>Oil Companies</li><li>Freight Forwarders &amp; Custom Brokers</li><li>Publishing and Advertising Companies</li><li>Construction and Real Estate Firms</li>
    </ul>
    <span class="tab">Why Use Us</span>
    <p>Anyone can sue a Debtor. It's not difficult to get nasty or to treat people who owe you money in a rude and unprofessional way.</p>
    <p>However, very few people have the skill, temperament and experience needed to effectively negotiate with Debtors, stakeholders, lawyers, as well as, court personnel, sheriffs and bankers to efficiently collect the most money possible in the least amount of time.</p>
    <p>We truly understand the nature of commercial debt. Collecting money is a specialized skill.</p>
    <svg class="wave" viewBox="0 0 190 60" preserveAspectRatio="none" aria-hidden="true">
      <path d="M0 60 L0 20 Q95 50 190 0 L190 60 Z" fill="var(--blue)"/>
    </svg>
  </div>

  <div class="panel">
    <div class="photo photo--city" role="img" aria-label="Faded black and white photograph of the New York City skyline"></div>
    <div class="contact">
      <div class="firm">Dorven &amp; Company PLLC</div>
      <div class="tag">Debt Collection Attorneys in New York State</div>
      <div class="who">MARCUS T. DORVEN, ESQUIRE</div>
      <div class="line">President</div>
      <div class="line">mdorven@dorvenlaw.com</div>
      <div class="line">(212) 555-0193 Cell</div>
      <div class="office">Fairbrook County Office</div>
      <div class="line">410 HARBOR VIEW ROAD, SUITE 12<br>FAIRBROOK, NEW YORK 10699<br>(Off Exit 4 on Route 9)</div>
      <div class="office">Mailing Address</div>
      <div class="line">55 LINDEN STREET, SUITE 300<br>NEW YORK, NEW YORK 10099</div>
      <div class="web">www.dorvenlaw.com</div>
      <div class="call">
        <svg width="22" height="22" viewBox="0 0 24 24" aria-hidden="true"><circle cx="12" cy="12" r="12" fill="var(--navy)"/><path d="M9 6l2 3-1.4 1.2a8 8 0 0 0 4.2 4.2L15 13l3 2-1 2.5c-5 .3-10-4.7-9.7-9.7z" fill="#fff"/></svg>
        <span>TOLL FREE: (877) 555-0142<br>LOCAL: (212) 555-0108<br>FAX: (917) 555-0118</span>
      </div>
    </div>
  </div>

  <div class="panel" style="padding:0">
    <div class="cover-head">
      <div class="firm">Dorven &amp; Company PLLC</div>
      <div class="sub">Debt Collection Attorneys</div>
    </div>
    <svg class="cover-shape" viewBox="0 0 190 320" preserveAspectRatio="none" aria-hidden="true">
      <polygon points="40,0 190,0 190,320 0,320 0,180" fill="var(--blue)"/>
      <polygon points="150,40 190,40 190,110" fill="var(--navy)"/>
    </svg>
    <div class="photo photo--library" role="img" aria-label="Blue-toned photograph of a law library with gavel and scales of justice"></div>
    <div class="cover-phone">
      <svg width="20" height="20" viewBox="0 0 24 24" aria-hidden="true"><circle cx="12" cy="12" r="11" fill="none" stroke="var(--navy)" stroke-width="1.5"/><path d="M9 6l2 3-1.4 1.2a8 8 0 0 0 4.2 4.2L15 13l3 2-1 2.5c-5 .3-10-4.7-9.7-9.7z" fill="var(--navy)"/></svg>
      (877) 555-0142
    </div>
  </div>
</section>

<section class="sheet sheet--inside">
  <div class="panel">
    <span class="tab">Who We Are</span>
    <p><em>DORVEN &amp; COMPANY, PLLC ("DORVEN")</em> is a New York based law firm devoted to the collection of accounts receivable and business debts.</p>
    <span class="tab">What We Do</span>
    <p>Within 24 to 72 hours of receiving a claim, we will verify the debt, investigate the Debtor, skip trace all known stakeholders and file a lawsuit with the intent of collecting the full amount due in the shortest time possible.</p>
    <p>We will use all legal means necessary to locate, identify, seize, or otherwise garnish a Debtor's assets and income, while always having an attorney available to speak directly with the Debtor to achieve an amicable resolution as quickly as possible.</p>
    <span class="tab">Our Mission</span>
    <p>Our mission is to protect our clients' bottom line, while preserving their reputation.</p>
    <p>We recognize and appreciate that your Debtor was once a trusted customer and may be a source of future revenue.</p>
    <p>We treat all Debtors with respect, while aggressively seeking to collect all monies owed.</p>
    <div class="photo photo--building" role="img" aria-label="Black and white photograph of courthouse columns"></div>
  </div>

  <div class="panel" style="padding-top:126px">
    <div class="photo photo--gavel" role="img" aria-label="Photograph of a wooden gavel, law books and brass scales"></div>
    <span class="tab tab--sm">Flexible Fee Structure</span>
    <p>We recognize that each claim is unique, therefore to better serve our clients we offer a variety of fee structures that meet the needs of our clients. Including:</p>
    <ul class="fees"><li>Contingency Fee</li><li>Flat Fee</li><li>Hourly fee</li><li>Monthly or Annual Retainer</li><li>Any combination of the above</li></ul>
    <span class="tab tab--sm">Handling Medical Receivables</span>
    <p>Medical receivables require a soft touch.</p>
    <p>Doctors and health organizations often write-off tens of thousands of dollars in unpaid deductibles and co-insurance which are rightfully due them out of fear that pursuing these debts will alienate, upset or offend their patients.</p>
    <p>We offer non-legal, HIPAA compliant collection methods which can effectively and consistently turn these otherwise uncollectible assets into real cash.</p>
    <p>Using a combination of letters and phone calls, our staff contacts patients in a professional and friendly manner to arrange for payments, as small as $15 per month, encouraging them to pay all monies owed.</p>
  </div>

  <div class="panel">
    <p>Before extending credit, we will review the applicant's payment history, public records, trade references and financial formation and other relevant data in order to determine creditworthiness.</p>
    <p>As your credit advisor, we will provide a full recommendation with regard to the amount and terms credit should be offered to specific customers.</p>
    <p>Once a credit determination is made, we can provide the client with a credit agreement detailing each parties' obligations. Using such agreements minimizes risk, while enhancing our clients' professional stature with their customers.</p>
    <span class="tab tab--sm">Keeping You In Compliance</span>
    <p>As your collection attorney and advisor, we will assure that your collection practices are in full compliance with all applicable Federal and State laws. Including The Fair Debt Collection Practices Act (FDCPA) and The Health Insurance Portability and Accountability Act (HIPAA).</p>
    <span class="tab tab--sm">State-of-the-Art Technology</span>
    <p>Our firm prides itself on utilizing the state-of-the-art technology in law office management, telephony, cyber security, document production, and cloud storage.</p>
    <p>Our clients can be assured that their critical business data is stored in a safe, secure, and confidential environment, while allowing us to seamlessly handle a large and ever growing book of business in a timely manner.</p>
  </div>
</section>

</body>
</html>
```